Brightvale Marketing Banner for emails to customers

Hi Marketing Team The information is to be a nice banner say half page on Marketing our Services to prospective customers, this is embedded into an email so something nice with the content that I will provide. Based on a nice background to highlight our service portfolio aligned to our website
www.brightvale-example.com.au

```html
<!DOCTYPE html>
<html lang="en">
<head>
<meta charset="utf-8">
<title>Brightvale – Cleaning Experts</title>
<link rel="stylesheet" href="https://fonts.googleapis.com/css2?family=Montserrat:wght@400;500;600;700&display=swap">
<style>
  :root {
    --orange: #ff4f05;
    --navy: #0a3a73;
    --ink: #1d1d1f;
    --white: #ffffff;
  }
  * { margin: 0; padding: 0; box-sizing: border-box; }
  html, body { width: 1200px; height: 960px; overflow: hidden; background: var(--white); }
  .banner {
    position: relative;
    width: 1200px;
    height: 960px;
    overflow: hidden;
    background: var(--white);
    font-family: "Montserrat", sans-serif;
    color: var(--ink);
  }
  .art { position: absolute; inset: 0; width: 1200px; height: 960px; }

  .brand {
    position: absolute; left: 56px; top: 58px;
    display: flex; align-items: center; gap: 12px;
  }
  .brand-dot { width: 44px; height: 44px; border-radius: 50%; background: var(--navy); }
  .brand-name { font-size: 36px; font-weight: 600; color: var(--navy); letter-spacing: -0.5px; }

  .headline { position: absolute; left: 52px; top: 162px; line-height: 0.95; font-weight: 700; }
  .headline span { display: block; font-size: 100px; letter-spacing: -1px; }
  .headline .line-orange { color: var(--orange); }
  .headline .line-navy { color: var(--navy); margin-top: 6px; }

  .tenure { position: absolute; left: 56px; top: 394px; font-size: 33px; font-weight: 400; letter-spacing: 0.3px; }
  .tenure strong { font-weight: 700; }
  .rule { position: absolute; left: 56px; top: 450px; width: 123px; height: 3px; background: var(--orange); }

  .services-title { position: absolute; left: 57px; top: 508px; font-size: 30px; font-weight: 500; color: var(--navy); letter-spacing: 0.5px; }
  .services-title em { font-style: normal; color: var(--orange); }

  .services { position: absolute; left: 55px; top: 560px; list-style: none; }
  .services li { display: flex; align-items: center; gap: 9px; height: 26.5px; font-size: 17.5px; font-weight: 500; color: #2a2a2a; }
  .services svg { width: 16px; height: 16px; flex: none; }

  .call { position: absolute; left: 56px; top: 726px; font-size: 31px; font-weight: 500; letter-spacing: 0.5px; }
  .phone { position: absolute; left: 54px; top: 766px; font-size: 47px; font-weight: 700; color: var(--orange); letter-spacing: 0.5px; }
  .contact { position: absolute; left: 56px; top: 824px; font-size: 19.5px; font-weight: 500; line-height: 25px; }

  .offer {
    position: absolute; left: 468px; top: 748px; width: 300px;
    text-align: center; color: var(--white); font-weight: 500;
  }
  .offer-figure { font-size: 74px; font-weight: 600; line-height: 1; }
  .offer-text { font-size: 24.5px; line-height: 31px; margin-top: 4px; }
</style>
</head>
<body>
<main class="banner">
  <svg class="art" viewBox="0 0 1200 960" aria-hidden="false">
    <defs>
      <linearGradient id="kitchen" x1="0" y1="0" x2="1" y2="1">
        <stop offset="0" stop-color="#eceff2"/>
        <stop offset="0.45" stop-color="#c9d0d4"/>
        <stop offset="0.7" stop-color="#e9ebec"/>
        <stop offset="1" stop-color="#8f9092"/>
      </linearGradient>
    </defs>
    <polygon role="img" aria-label="Photo of a bright white kitchen with a stone benchtop, steel sink, range hood and tiled splashback"
             points="800,0 1200,0 1200,960 428,960" fill="url(#kitchen)"/>
    <polygon class="offer-shape" points="596,540 428,960 840,960" fill="var(--orange)"/>
  </svg>

  <div class="brand">
    <span class="brand-dot"></span>
    <span class="brand-name">Brightvale</span>
  </div>

  <h1 class="headline">
    <span class="line-orange">CLEANING</span>
    <span class="line-navy">EXPERTS</span>
  </h1>

  <p class="tenure">IN BUSINESS <strong>FOR 15 YEARS</strong></p>
  <div class="rule"></div>

  <h2 class="services-title">PORTFOLIO <em>OF SERVICES</em></h2>
  <ul class="services">
    <li><svg viewBox="0 0 16 16"><circle cx="8" cy="8" r="8" fill="#ff4f05"/><path d="M4.5 8.2l2.3 2.2 4.7-4.6" fill="none" stroke="#fff" stroke-width="1.8" stroke-linecap="round" stroke-linejoin="round"/></svg>Equipment Sundae Machine Cleaning Service</li>
    <li><svg viewBox="0 0 16 16"><circle cx="8" cy="8" r="8" fill="#ff4f05"/><path d="M4.5 8.2l2.3 2.2 4.7-4.6" fill="none" stroke="#fff" stroke-width="1.8" stroke-linecap="round" stroke-linejoin="round"/></svg>Detailed Kitchen Cleaning and Vat Boil Outs</li>
    <li><svg viewBox="0 0 16 16"><circle cx="8" cy="8" r="8" fill="#ff4f05"/><path d="M4.5 8.2l2.3 2.2 4.7-4.6" fill="none" stroke="#fff" stroke-width="1.8" stroke-linecap="round" stroke-linejoin="round"/></svg>Gurney High Pressure and Playground Cleaning</li>
    <li><svg viewBox="0 0 16 16"><circle cx="8" cy="8" r="8" fill="#ff4f05"/><path d="M4.5 8.2l2.3 2.2 4.7-4.6" fill="none" stroke="#fff" stroke-width="1.8" stroke-linecap="round" stroke-linejoin="round"/></svg>General Facility Maintenance</li>
  </ul>

  <p class="call">CALL US TODAY</p>
  <p class="phone">1300 555 019</p>
  <p class="contact">service@brightvale-example.com.au<br>www.brightvale-example.com.au</p>

  <div class="offer">
    <p class="offer-figure">20%</p>
    <p class="offer-text">of discount on<br>your first cleaning<br>order</p>
  </div>
</main>
</body>
</html>
```